Poster for List of Company Values

We need a poster to outline our Values which will be displayed in our office as well as posted on our website and other platforms (so need to allow for some flexibly in its application).

File attached outlines what we currently have with design and also our company style guide.

Note that we are looking for a modern, clean look, which still represents our core activities of construction and environmental services.

You can also reference our website here:

https://corvellagroup.com.au/

Happy to answer any questions you might have.

Thanks for your interest,
Wynn

Target Market(s)

Internal and External clients

Industry/Entity Type

Construction, water and recycling

Font styles to use
Sans Serif

Requirements
Must have
• All values on the one page. Graphic to represent each value. Also needs to use company logo
Nice to have
• Preference for poster to be orientated in landscape
Should not have
• Do not follow example provided, this is only to demonstrate what we have to date and also the text required

```html
<!DOCTYPE html>
<html lang="en">
<head>
<meta charset="utf-8">
<title>Corvella Group – Our Values</title>
<link rel="stylesheet" href="https://fonts.googleapis.com/css2?family=Open+Sans:ital,wght@0,300;0,600;1,400&display=swap">
<style>
  :root {
    --paper: #ffffff;
    --ink-light: #ffffff;
    --grey-stripe: #c9c9c9;
    --grey-block: #8a8a8a;
    --logo-ink: #3d3d3d;
    --logo-mark: #243f8f;
    --green-top: #00b050;
    --green-bottom: #05803b;
    --yellow-left: #ffc400;
    --yellow-right: #e3ae3d;
    --blue-top: #0071c2;
    --blue-bottom: #1062a6;
    --orange-left: #d86b37;
    --orange-right: #f08a2f;
    --cyan-left: #1a8fc3;
    --cyan-right: #00b1f1;
    --pink-top: #d72c80;
    --pink-bottom: #ff2d92;
    --icon-tint: rgba(255, 255, 255, 0.18);
  }
  * { margin: 0; padding: 0; box-sizing: border-box; }
  html, body {
    width: 1001px; height: 1200px; overflow: hidden;
    background: var(--paper);
  }
  .poster {
    position: relative; width: 1001px; height: 1200px; overflow: hidden;
    background: var(--paper);
    font-family: "Open Sans", sans-serif;
    color: var(--ink-light);
  }
  .stripes { position: absolute; left: 0; top: 0; }
  .grey-block { position: absolute; background: var(--grey-block); opacity: 0.75; }

  .value { position: absolute; overflow: hidden; }
  .value--loyal { left: 185px; top: 61px; width: 242px; height: 397px;
    background: linear-gradient(180deg, var(--green-top), var(--green-bottom)); }
  .value--initiative { left: 448px; top: 196px; width: 433px; height: 262px;
    background: linear-gradient(90deg, var(--yellow-left), var(--yellow-right)); }
  .value--team { left: 118px; top: 477px; width: 422px; height: 271px;
    background: linear-gradient(180deg, var(--blue-top), var(--blue-bottom)); }
  .value--respect { left: 561px; top: 477px; width: 278px; height: 243px;
    background: linear-gradient(90deg, var(--orange-left), var(--orange-right)); }
  .value--positive { left: 561px; top: 739px; width: 320px; height: 242px;
    background: linear-gradient(90deg, var(--cyan-left), var(--cyan-right)); }
  .value--open { left: 185px; top: 769px; width: 356px; height: 369px;
    background: linear-gradient(180deg, var(--pink-top), var(--pink-bottom)); }

  .lead, .title {
    position: absolute; font-weight: 300; line-height: 1; white-space: nowrap;
  }
  .desc {
    position: absolute; font-style: italic; font-weight: 400;
    font-size: 14px; line-height: 17px; white-space: nowrap;
  }
  .icon { position: absolute; background: var(--icon-tint); border-radius: 10px; }

  .logo {
    position: absolute; left: 585px; top: 1040px;
    display: flex; align-items: center; gap: 14px;
  }
  .logo__square { width: 58px; height: 58px; background: var(--logo-mark); }
  .logo__name {
    font-family: "Open Sans", sans-serif; font-weight: 600;
    font-size: 30px; line-height: 32px; color: var(--logo-ink);
  }
</style>
</head>
<body>
<main class="poster">

  <svg class="stripes" width="1001" height="200" viewBox="0 0 1001 200" aria-hidden="true">
    <g stroke="var(--grey-stripe)" stroke-width="22" stroke-linecap="round">
      <line x1="722" y1="45" x2="760" y2="-10"/>
      <line x1="759" y1="93" x2="830" y2="-10"/>
      <line x1="790" y1="159" x2="925" y2="-10"/>
    </g>
  </svg>

  <div class="grey-block" style="left:448px;top:116px;width:74px;height:65px" role="img" aria-label="Grey square cluster decoration"></div>
  <div class="grey-block" style="left:848px;top:477px;width:52px;height:44px" role="img" aria-label="Grey square cluster decoration"></div>
  <div class="grey-block" style="left:107px;top:770px;width:65px;height:59px" role="img" aria-label="Grey square cluster decoration"></div>

  <section class="value value--loyal">
    <span class="lead" style="left:14px;top:5px;font-size:44px">be</span>
    <span class="title" style="left:12px;top:44px;font-size:68px">LOYAL</span>
    <div class="icon" style="left:0;top:136px;width:181px;height:180px" role="img" aria-label="Line icon of a briefcase above a handshake"></div>
    <p class="desc" style="left:14px;top:338px">We take care of our own and<br>provide opportunities to listen<br>and support each other.</p>
  </section>

  <section class="value value--initiative">
    <span class="lead" style="left:26px;top:-14px;font-size:80px">show</span>
    <span class="title" style="left:28px;top:50px;font-size:82px">INITIATIVE</span>
    <p class="desc" style="left:20px;top:210px">We celebrate and recognize our own<br>and encourage forward thinking.</p>
    <div class="icon" style="left:318px;top:140px;width:115px;height:122px" role="img" aria-label="Line icon of a hand holding a flag"></div>
  </section>

  <section class="value value--team">
    <div class="icon" style="left:0;top:0;width:150px;height:146px" role="img" aria-label="Line icon of three hands joined in a circle"></div>
    <span class="lead" style="right:31px;top:3px;font-size:71px">think</span>
    <span class="title" style="right:31px;top:55px;font-size:86px">TEAM</span>
    <p class="desc" style="left:28px;top:190px">We communicate effectively and<br>work as a team by helping and<br>supporting each other.</p>
  </section>

  <section class="value value--respect">
    <p class="desc" style="left:18px;top:14px">We value the<br>diversity<br>and opinions<br>of all.</p>
    <div class="icon" style="left:125px;top:18px;width:153px;height:120px" role="img" aria-label="Line icon of two thumbs up"></div>
    <span class="lead" style="left:26px;top:120px;font-size:52px">show</span>
    <span class="title" style="left:24px;top:166px;font-size:56px">RESPECT</span>
  </section>

  <section class="value value--positive">
    <span class="lead" style="left:27px;top:-3px;font-size:43px">be</span>
    <span class="title" style="left:27px;top:31px;font-size:58px">POSITIVE</span>
    <p class="desc" style="left:16px;top:128px">SMILE : We are<br>solutions focused and<br>encourage a positive<br>attitude turning a<br>negative into a<br>positive.</p>
    <div class="icon" style="left:178px;top:108px;width:122px;height:134px" role="img" aria-label="Line icon of a head with a glowing plus sign"></div>
  </section>

  <section class="value value--open">
    <span class="title" style="left:33px;top:18px;font-size:55px">beOPEN</span>
    <span class="title" style="left:33px;top:62px;font-size:55px"><span style="font-size:40px">and</span>HONEST</span>
    <div class="icon" style="left:0;top:159px;width:128px;height:174px" role="img" aria-label="Line icon of a person holding a heart"></div>
    <p class="desc" style="left:160px;top:250px">We are clear and open<br>with each other, and<br>provide an approachable<br>and friendly<br>environment.</p>
  </section>

  <div class="logo">
    <span class="logo__square" aria-hidden="true"></span>
    <span class="logo__name">CORVELLA<br>Group</span>
  </div>

</main>
</body>
</html>
```